Sandwich Board and Poster design promoting a medical aesthetic clinic

I am looking for a clean, modern and relaxing design promoting a medical physician-led aesthetic clinic.
Services offered are neuromodulator treatment (Quelvo) and Dermal Fillers.
Logo must be included.
Use the tag line "Refresh your look, revive your spirit."
Address is 204-205 27361 92 Ave, Surrey, V7K 2M4
604-555-0148
email - info@lumawellpine.ca
www.lumawellpine.ca

```html
<!DOCTYPE html>
<html lang="en">
<head>
<meta charset="utf-8">
<title>Lumawell Pine – Banner</title>
<link href="https://fonts.googleapis.com/css2?family=Roboto:wght@400;500&display=swap" rel="stylesheet">
<style>
  :root {
    --stage: #000000;
    --paper: #ffffff;
    --ink: #111111;
    --brand-ink: #333333;
    --gold: #a8893d;
    --gold-bright: #c9a43a;
    --band-text: #ffffff;
    --photo-dark: #1f1510;
    --photo-brown: #6e4a36;
    --photo-skin: #c89a7c;
    --photo-blonde: #e3cdb2;
    --photo-pale: #f3e6dc;
  }
  * { margin: 0; padding: 0; box-sizing: border-box; }
  html, body {
    width: 1200px; height: 1200px; overflow: hidden;
    background: var(--stage);
    font-family: "Roboto", Arial, sans-serif;
  }
  .banner {
    position: absolute; left: 115px; top: 358px;
    width: 969px; height: 483px;
    background: var(--paper);
    overflow: hidden;
  }
  .banner__photo {
    position: absolute; left: 0; top: 0;
    width: 430px; height: 448px;
    background:
      radial-gradient(ellipse 120px 170px at 240px 200px, rgba(176,120,88,0.9), rgba(176,120,88,0) 100%),
      radial-gradient(ellipse 110px 200px at 370px 200px, rgba(243,226,214,0.95), rgba(243,226,214,0) 100%),
      radial-gradient(ellipse 90px 260px at 300px 120px, rgba(227,205,178,0.8), rgba(227,205,178,0) 100%),
      linear-gradient(90deg,
        var(--photo-dark) 0%, var(--photo-dark) 18%, var(--photo-brown) 38%,
        var(--photo-skin) 55%, var(--photo-blonde) 68%, var(--photo-pale) 84%, var(--paper) 100%);
  }
  .banner__url {
    position: absolute; right: 22px; top: 14px;
    font-size: 18px; color: var(--ink);
  }
  .brand {
    position: absolute; left: 482px; top: 97px; width: 400px;
    text-align: center;
  }
  .brand__mark {
    display: block; margin: 0 auto 44px;
  }
  .brand__name {
    font-size: 38px; line-height: 1; font-weight: 400; letter-spacing: 6px;
    color: var(--brand-ink); white-space: nowrap;
  }
  .banner__tagline {
    position: absolute; left: 430px; width: 504px; top: 381px;
    text-align: center; font-size: 22px; color: var(--ink);
  }
  .contact-band {
    position: absolute; left: 0; bottom: 0;
    width: 100%; height: 35px; background: var(--gold);
    color: var(--band-text); font-size: 18px;
  }
  .contact-band span { position: absolute; top: 6px; white-space: nowrap; }
  .contact-band__address { left: 73px; }
  .contact-band__phone { left: 467px; }
  .contact-band__email { left: 654px; }
</style>
</head>
<body>
  <section class="banner">
    <div class="banner__photo" role="img" aria-label="Photograph of two women in side profile showing smooth, refreshed skin"></div>
    <p class="banner__url">www.lumawellpine.ca</p>

    <div class="brand">
      <svg class="brand__mark" width="130" height="130" viewBox="0 0 130 130" aria-hidden="true">
        <circle cx="65" cy="65" r="62" fill="none" stroke="var(--gold-bright)" stroke-width="3"/>
      </svg>
      <p class="brand__name">LUMAWELL PINE</p>
    </div>

    <p class="banner__tagline">Refresh your look, revive your spirit.</p>

    <footer class="contact-band">
      <span class="contact-band__address">204-205 27361 92 Ave, Surrey, V7K 2M4</span>
      <span class="contact-band__phone">Tel: 604-555-0148</span>
      <span class="contact-band__email">email: info@lumawellpine.ca</span>
    </footer>
  </section>
</body>
</html>
```